VelloPath Business Card

Our company is called VelloPath and we are based in Tel Aviv, Israel. We create innovative and exciting methods for getting people on the web engaged with content. We need a cool yet professional business card that will represent our management level employees. keep in mind this is a start up company with a young atmosphere. You can be inspired by our logo (file attached, make sure you have the right font "Ubuntu-Condensed") Use the colors that are used in the logo and create a colourful and professional business card.

```html
<!DOCTYPE html>
<html lang="en">
<head>
<meta charset="utf-8">
<title>VelloPath Business Card</title>
<link rel="stylesheet" href="https://fonts.googleapis.com/css2?family=Ubuntu+Condensed&family=Ubuntu:wght@400;500&display=swap">
<style>
  :root {
    --stage: #2b2b2b;
    --charcoal: #3b3b3d;
    --paper: #ffffff;
    --ink: #222222;
    --ink-soft: #333333;
    --accent-blue: #1f7fcc;
    --dot-pink: #e8247a;
    --dot-purple: #8e2f8e;
    --dot-blue: #45addf;
    --dot-yellow: #fcd116;
    --dot-green: #7dc142;
    --dot-orange: #f7a23c;
  }
  * { box-sizing: border-box; margin: 0; padding: 0; }
  html, body { width: 1200px; height: 800px; overflow: hidden; }
  body {
    position: relative;
    background: var(--stage);
    font-family: "Ubuntu", sans-serif;
    color: var(--ink);
  }
  .card {
    position: absolute;
    width: 480px;
    height: 273px;
    border-radius: 22px;
    overflow: hidden;
  }
  .card--front-a { left: 100px; top: 87px; }
  .card--back-a  { left: 623px; top: 87px; }
  .card--front-b { left: 100px; top: 437px; }
  .card--back-b  { left: 623px; top: 437px; }

  .front-pattern {
    position: absolute; inset: 0;
    background:
      linear-gradient(rgba(59,59,61,.45), rgba(59,59,61,.45)),
      linear-gradient(135deg,
        var(--dot-yellow) 0%,
        var(--dot-pink) 22%,
        var(--dot-purple) 42%,
        var(--dot-blue) 62%,
        var(--dot-green) 80%,
        var(--dot-orange) 100%);
  }
  .wordmark {
    position: absolute;
    font-family: "Ubuntu Condensed", "Ubuntu", sans-serif;
    font-weight: 400;
    line-height: 1;
    white-space: nowrap;
    letter-spacing: 0.5px;
  }
  .front-wordmark { color: var(--paper); }
  .card--front-a .front-wordmark { right: 24px; bottom: 22px; font-size: 62px; }
  .card--front-b .front-wordmark { right: 22px; bottom: 16px; font-size: 80px; }

  .card--back { background: var(--paper); }
  .back-pattern {
    position: absolute; inset: 0;
    background:
      radial-gradient(circle at 20% 30%, rgba(232,36,122,.05), transparent 35%),
      radial-gradient(circle at 75% 25%, rgba(69,173,223,.05), transparent 35%),
      radial-gradient(circle at 45% 80%, rgba(252,209,22,.06), transparent 35%),
      var(--paper);
  }
  .brand-dot {
    position: absolute;
    border-radius: 50%;
    background: var(--dot-pink);
  }
  .back-wordmark { color: var(--ink); }
  .contact { position: absolute; }
  .contact__name { font-weight: 400; color: var(--ink); line-height: 1; }
  .contact__role { color: var(--accent-blue); line-height: 1; }
  .contact__address { color: var(--ink-soft); }
  .contact__lines {
    color: var(--ink-soft);
    border-left: 2px solid var(--accent-blue);
  }

  .card--back-a .brand-dot { left: 110px; top: 80px; width: 62px; height: 62px; }
  .card--back-a .back-wordmark { left: 46px; top: 168px; font-size: 40px; }
  .card--back-a .contact { left: 288px; top: 52px; }
  .card--back-a .contact__name { font-size: 28px; }
  .card--back-a .contact__role { font-size: 13px; margin: 8px 0 0 3px; }
  .card--back-a .contact__address { font-size: 13px; line-height: 19px; margin-top: 20px; }
  .card--back-a .contact__lines { font-size: 13px; line-height: 18px; margin-top: 14px; padding-left: 6px; }

  .card--back-b .brand-dot { left: 110px; top: 78px; width: 76px; height: 76px; }
  .card--back-b .back-wordmark { left: 34px; top: 176px; font-size: 50px; }
  .card--back-b .contact { left: 302px; top: 51px; }
  .card--back-b .contact__name { font-size: 28px; }
  .card--back-b .contact__role { font-size: 13px; margin: 8px 0 0 4px; }
  .card--back-b .contact__address { font-size: 13px; line-height: 19px; margin-top: 20px; }
  .card--back-b .contact__lines { font-size: 13px; line-height: 18px; margin-top: 14px; padding-left: 6px; }
</style>
</head>
<body>

  <section class="card card--front card--front-a">
    <div class="front-pattern" role="img" aria-label="Pattern of overlapping pink, purple, blue, yellow, green and orange circles on charcoal"></div>
    <div class="wordmark front-wordmark">vellopath</div>
  </section>

  <section class="card card--back card--back-a">
    <div class="back-pattern" role="img" aria-label="Faint pattern of pale coloured circles on white"></div>
    <div class="brand-dot"></div>
    <div class="wordmark back-wordmark">vellopath</div>
    <div class="contact">
      <p class="contact__name">Noa Shaked</p>
      <p class="contact__role">Co-Founder &amp; CEO</p>
      <p class="contact__address">57 Hamasger Street,<br>Tel Aviv, Israel 61570</p>
      <p class="contact__lines">+972-503816274<br>noa@vellopath.com<br>www.vellopath.com</p>
    </div>
  </section>

  <section class="card card--front card--front-b">
    <div class="front-pattern" role="img" aria-label="Pattern of overlapping pink, purple, blue, yellow, green and orange circles on charcoal"></div>
    <div class="wordmark front-wordmark">vellopath</div>
  </section>

  <section class="card card--back card--back-b">
    <div class="back-pattern" role="img" aria-label="Faint pattern of pale coloured circles on white"></div>
    <div class="brand-dot"></div>
    <div class="wordmark back-wordmark">vellopath</div>
    <div class="contact">
      <p class="contact__name">Noa Shaked</p>
      <p class="contact__role">Co-Founder &amp; CEO</p>
      <p class="contact__address">57 Hamasger Street,<br>Tel Aviv, Israel 61570</p>
      <p class="contact__lines">+972-503816274<br>noa@vellopath.com<br>www.vellopath.com</p>
    </div>
  </section>

</body>
</html>
```